Executive Coach needs elegant business card design

I need a business card design which includes following info: name, email (same as name, @vessiermail.com), phone. I'd put that on one side. On the other side i'd like some graphic indicating what i do:
- using questions to help people get great results
- encourage people to try different solutions to overcome old problems
- untangling the mental knot that traps people in vicious circles
- question mental models to get people to see a different point of view.

I'd like an elegant design. Bonus points for providing a different twist on things. I've included 2 designs I started with. Feel free to improve or discard them :-)

```html
<!DOCTYPE html>
<html lang="en">
<head>
<meta charset="utf-8">
<title>Laurent Vessier – Executive Coach</title>
<link rel="stylesheet" href="https://fonts.googleapis.com/css2?family=Urbanist:wght@300;400;700;800&family=Roboto+Condensed:wght@700&display=swap">
<style>
  :root {
    --cyan: #5cf9fa;
    --cyan-pale: #8ff9fb;
    --icon-disc: #c6f8fa;
    --icon-shadow: #9eaaab;
    --ink: #111111;
    --silver-light: #ffffff;
    --silver-mid: #e4e9ea;
    --silver-dark: #bcc6c7;
  }
  * { margin: 0; padding: 0; box-sizing: border-box; }
  html, body { width: 791px; height: 1200px; overflow: hidden; }
  body { font-family: "Urbanist", sans-serif; color: var(--ink); }

  .card {
    position: relative;
    width: 791px;
    height: 1200px;
    overflow: hidden;
    background: linear-gradient(148deg,
      var(--silver-mid) 0%,
      var(--silver-light) 8%,
      var(--silver-dark) 22%,
      var(--silver-light) 40%,
      var(--silver-mid) 52%,
      var(--silver-dark) 66%,
      var(--silver-light) 84%,
      var(--silver-mid) 100%);
  }

  .brand {
    position: absolute;
    top: 176px;
    left: 0;
    width: 791px;
    display: flex;
    justify-content: center;
    align-items: center;
    gap: 14px;
    font-size: 32px;
    font-weight: 400;
    letter-spacing: 1px;
  }
  .brand-dot {
    width: 20px; height: 20px;
    border-radius: 50%;
    background: var(--cyan);
  }

  .title-banner { position: absolute; left: 0; top: 0; }

  .job-title {
    position: absolute;
    left: 188px;
    top: 398px;
    white-space: nowrap;
    line-height: 1;
  }
  .job-title .light { font-size: 48px; font-weight: 400; letter-spacing: 2px; }
  .job-title .bold {
    font-family: "Roboto Condensed", sans-serif;
    font-size: 64px;
    font-weight: 700;
    margin-left: 10px;
  }

  .name {
    position: absolute;
    left: 155px;
    top: 485px;
    height: 87px;
    display: flex;
    align-items: center;
    white-space: nowrap;
  }
  .name .first {
    background: var(--cyan);
    height: 87px;
    padding: 0 6px 0 11px;
    font-size: 64px;
    font-weight: 300;
    line-height: 87px;
  }
  .name .last {
    font-size: 62px;
    font-weight: 800;
    margin-left: 10px;
    line-height: 87px;
  }

  .contact-icon { position: absolute; left: 338px; width: 75px; height: 75px; }
  .contact-icon.mail { top: 629px; }
  .contact-icon.phone { top: 791px; }

  .contact-line {
    position: absolute;
    left: 0;
    width: 791px;
    text-align: center;
    font-weight: 400;
    white-space: nowrap;
  }
  .contact-line.email { top: 706px; font-size: 40px; letter-spacing: 0.5px; }
  .contact-line.tel { top: 874px; font-size: 41px; letter-spacing: 3px; }
</style>
</head>
<body>
<main class="card">
  <div class="brand"><span class="brand-dot"></span><span>Vessier Coaching</span></div>

  <svg class="title-banner" width="791" height="600" viewBox="0 0 791 600" aria-hidden="true">
    <polygon points="219,355 370,373 181,402 181,373 219,373" fill="var(--cyan-pale)"/>
    <polygon points="181,402 600,336 600,468 181,468" fill="var(--cyan)"/>
  </svg>

  <h2 class="job-title"><span class="light">Executive</span><span class="bold">Coach</span></h2>

  <h1 class="name"><span class="first">Laurent</span><span class="last">Vessier</span></h1>

  <svg class="contact-icon mail" viewBox="0 0 75 75" aria-hidden="true">
    <defs><clipPath id="disc-mail"><circle cx="37.5" cy="37.5" r="37.5"/></clipPath></defs>
    <circle cx="37.5" cy="37.5" r="37.5" fill="var(--icon-disc)"/>
    <polygon clip-path="url(#disc-mail)" points="20,48 55,28 90,63 55,98" fill="var(--icon-shadow)"/>
    <rect x="20" y="28" width="35" height="20" rx="2" fill="var(--icon-disc)" stroke="var(--ink)" stroke-width="3"/>
    <polyline points="21,30 37.5,41 54,30" fill="none" stroke="var(--ink)" stroke-width="3"/>
  </svg>
  <p class="contact-line email">laurent.vessier@vessiermail.com</p>

  <svg class="contact-icon phone" viewBox="0 0 75 75" aria-hidden="true">
    <defs><clipPath id="disc-phone"><circle cx="37.5" cy="37.5" r="37.5"/></clipPath></defs>
    <circle cx="37.5" cy="37.5" r="37.5" fill="var(--icon-disc)"/>
    <polygon clip-path="url(#disc-phone)" points="28,57 46,17 90,61 72,101" fill="var(--icon-shadow)"/>
    <rect x="28" y="17" width="18" height="40" rx="3" fill="var(--icon-disc)" stroke="var(--ink)" stroke-width="3"/>
    <line x1="31" y1="48" x2="43" y2="48" stroke="var(--ink)" stroke-width="2"/>
    <circle cx="37" cy="52.5" r="1.6" fill="var(--ink)"/>
  </svg>
  <p class="contact-line tel">61843527</p>
</main>
</body>
</html>
```